Label and packaging - Lune de Sable

We are after label and pack design for a product called Lune de Sable. This product is a blend of Pinot Gris and Apple Cider.

Lune de Sable:

The packaging needs to accomplish the following: quickly explain what the product is, establish as a premium price product and grab the eye. The package should also reflect the product innovation.

Quickly Explain What the Product Is:

Lune de Sable is a nice name that could lift the image – but no one will have any idea what the product is by the name. Consider that a consumer will be staring at a shelf, then the bottle for maybe two to three seconds before moving on to another bottle. In those three seconds we need to make certain that they understand that the product is a blend of wine and cider. Lune de Sable will not support this on its own.

Suggestion is to use words like Wine, Cider, Orchard, Vine, Apple, Heirloom, Exotic and make it simple. Perhaps a sticker that says “50% Wine/50% Apple Cider” that sits on the neck of every bottle. They need to quickly ‘get it”. Imagery will assist as well. Consider a hybrid 50/50 image of wine grapes and apples to tell the story.

Establish a Premium Price Point:

The label needs to say high quality in the package and the font. Have fun with the shipper – this is where you can have a field day with imagery and fun buzz words – we love the idea of a busy shipper that tells the story with a clean and smart looking bottle.

Target Market(s)

This is a premium product targeted at females of age 25-45.

Industry/Entity Type

Consumer

Colors
ec1f27
9bcb3c

Requirements
Must have
• Label design on a burgundy bottle with a screw cap, see here for bottle shape: http://www.vexlabottles.co.nz/wine/#/?view=thumbs&segments=41&colors=&capacityMin=187&capacityMax=750&heightMin=171&heightMax=334&labelMin=44&labelMax=168&neckMin=0&neckMax=1000

Packaging design on a 12 x 750ml carton. This sort of thing: https://www.brakunstores.com.au/images/photo06.jpg

Nice to have
• We have attached some examples of a concept we quite like but it's not bright enough.

```html
<!DOCTYPE html>
<html lang="en">
<head>
<meta charset="utf-8">
<title>Lune de Sable – Label Designs</title>
<link rel="stylesheet" href="https://fonts.googleapis.com/css2?family=Lato:wght@300;400;700&display=swap">
<style>
  :root {
    --canvas-bg: #ffffff;
    --ink-light: #ffffff;
    --green-light: #9bcb3c;
    --green-mid: #6aa92f;
    --green-deep: #3f7f22;
    --green-band: #3a7d2c;
    --red-light: #e0434a;
    --red-mid: #b71c26;
    --red-deep: #7e1019;
    --red-band: #ec1f27;
  }

  * { box-sizing: border-box; margin: 0; padding: 0; }

  html, body {
    width: 773px;
    height: 1200px;
    overflow: hidden;
    background: var(--canvas-bg);
  }

  .label-sheet {
    position: relative;
    width: 773px;
    height: 1200px;
    display: flex;
    justify-content: center;
    align-items: center;
    gap: 40px;
  }

  .label {
    position: relative;
    width: 330px;
    height: 490px;
    overflow: hidden;
    font-family: "Lato", Arial, sans-serif;
    color: var(--ink-light);
  }

  .label__photo {
    position: absolute;
    inset: 0;
  }

  .label--green .label__photo {
    background:
      radial-gradient(ellipse 75% 60% at 45% 38%, var(--green-light) 0%, var(--green-mid) 55%, var(--green-deep) 100%);
  }

  .label--red .label__photo {
    background:
      radial-gradient(ellipse 75% 60% at 45% 38%, var(--red-light) 0%, var(--red-mid) 55%, var(--red-deep) 100%);
  }

  .label__title {
    position: absolute;
    left: 0;
    right: 0;
    top: 278px;
    text-align: center;
    font-weight: 400;
    font-size: 58px;
    line-height: 1.02;
    letter-spacing: 0.5px;
    text-transform: uppercase;
    white-space: nowrap;
  }

  .label__title span { display: block; }

  .label__band {
    position: absolute;
    left: 14px;
    right: 14px;
    bottom: 10px;
    height: 40px;
    display: flex;
    flex-direction: column;
    justify-content: center;
    align-items: center;
    font-weight: 400;
    font-size: 10.5px;
    line-height: 1.35;
    letter-spacing: 0.4px;
    text-transform: uppercase;
    text-align: center;
    white-space: nowrap;
  }

  .label--green .label__band { background: var(--green-band); }
  .label--red .label__band { background: var(--red-band); }
</style>
</head>
<body>
  <main class="label-sheet">
    <article class="label label--green">
      <div class="label__photo" role="img" aria-label="Close-up photograph of a green apple with its stem, filling the label"></div>
      <h1 class="label__title"><span>Lune</span><span>de Sable</span></h1>
      <p class="label__band">
        <span>Blend of New Zealand Pinot Gris</span>
        <span>and Sparkling Apple Cider</span>
      </p>
    </article>

    <article class="label label--red">
      <div class="label__photo" role="img" aria-label="Close-up photograph of a red apple with its stem, filling the label"></div>
      <h2 class="label__title"><span>Lune</span><span>de Sable</span></h2>
      <p class="label__band">
        <span>Blend of New Zealand Pinot Gris</span>
        <span>and Sparkling Apple Cider</span>
      </p>
    </article>
  </main>
</body>
</html>
```